Brantwell Group needs a business card design

We need a new business card design using the logo recently selected in a logo competition on Pixel Forum. Our business is a consultancy specializing in aviation and energy and the winning business card design will promote an image of precision and professionalism with creativity.

Please use the logo with the name on the front of the card and use a complementary font. Make the back white with either the light grey or dark grey logo.

Target Market(s)

Senior finance and legal leaders at aviation and energy companies

Industry/Entity Type

Management Consulting

Contact Information for Business Card

Peter Haldane
President
Brantwell Group

www.brantwellgroup.example

(555) 304-6198
ph@brantwellgroup.example

Requirements
Must have
• Professional font that goes well with the logo font

```html
<!DOCTYPE html>
<html lang="en">
<head>
<meta charset="utf-8">
<title>Brantwell Group Business Card</title>
<link href="https://fonts.googleapis.com/css2?family=Source+Sans+3:wght@400;600;700&display=swap" rel="stylesheet">
<style>
  :root {
    --stage: #161616;
    --card-front: #f3f3f3;
    --card-back: #ffffff;
    --navy: #1c3766;
    --ink: #1a1a1a;
    --grey: #5f5f5f;
    --mark-grey: #6a6a6a;
  }
  * { margin: 0; padding: 0; box-sizing: border-box; }
  html, body {
    width: 1200px; height: 900px; overflow: hidden;
    background: var(--stage);
    font-family: "Source Sans 3", "Helvetica Neue", Arial, sans-serif;
  }
  .stage { position: relative; width: 1200px; height: 900px; }
  .card {
    position: absolute; top: 184px; height: 491px;
    border-radius: 13px; text-align: center;
  }
  .card--front { left: 299px; width: 301px; background: var(--card-front); }
  .card--back { left: 645px; width: 305px; background: var(--card-back); }

  .brand-name {
    position: absolute; left: 0; right: 0; top: 300px;
    color: var(--navy); font-weight: 400; line-height: 1;
  }
  .brand-name__primary { display: block; font-size: 35px; letter-spacing: 2px; text-transform: uppercase; }
  .brand-name__secondary { display: block; font-size: 17px; letter-spacing: 15px; margin-top: 14px; padding-left: 15px; text-transform: uppercase; }

  .person { position: absolute; left: 0; right: 0; top: 494px; top: 310px; }
  .person__name { font-size: 20px; font-weight: 700; color: var(--navy); line-height: 1; }
  .person__title { font-size: 13px; color: var(--ink); margin-top: 2px; }

  .contact { position: absolute; left: 0; right: 0; top: 392px; font-size: 14px; color: var(--ink); line-height: 21px; }
  .contact__line { display: flex; justify-content: center; align-items: center; gap: 4px; }
  .contact__icon { width: 10px; height: 10px; fill: var(--navy); }

  .back-name {
    position: absolute; left: 0; right: 0; top: 205px;
    color: var(--mark-grey); font-weight: 600; font-size: 40px;
    letter-spacing: 1px; text-transform: uppercase; line-height: 1.05;
  }
  .tagline { position: absolute; left: 0; right: 0; top: 388px; font-size: 17px; font-weight: 700; color: var(--navy); }
  .sectors { position: absolute; left: 0; right: 0; top: 418px; font-size: 15px; font-weight: 600; color: var(--grey); letter-spacing: 0.3px; word-spacing: 2px; }
</style>
</head>
<body>
<main class="stage">
  <section class="card card--front">
    <div class="brand-name" style="top:150px">
      <span class="brand-name__primary">Brantwell</span>
      <span class="brand-name__secondary">Group</span>
    </div>
    <div class="person" style="top:312px">
      <p class="person__name">Peter J. Haldane</p>
      <p class="person__title">President</p>
    </div>
    <div class="contact">
      <p class="contact__line">
        <svg class="contact__icon" viewBox="0 0 24 24" aria-hidden="true"><path d="M6.6 10.8a15.1 15.1 0 0 0 6.6 6.6l2.2-2.2a1 1 0 0 1 1-.25 11.4 11.4 0 0 0 3.6.57 1 1 0 0 1 1 1V20a1 1 0 0 1-1 1A17 17 0 0 1 3 4a1 1 0 0 1 1-1h3.5a1 1 0 0 1 1 1c0 1.25.2 2.45.57 3.6a1 1 0 0 1-.25 1z"/></svg>
        (555) 304-6198
      </p>
      <p class="contact__line">
        <svg class="contact__icon" viewBox="0 0 24 24" aria-hidden="true"><path d="M2 5h20v14H2z M2 5l10 8 10-8" fill="var(--navy)"/><path d="M3 6l9 7 9-7" fill="none" stroke="#f3f3f3" stroke-width="2"/></svg>
        ph@brantwellgroup.example
      </p>
    </div>
  </section>

  <section class="card card--back">
    <p class="back-name">Brantwell<br>Group</p>
    <p class="tagline">Finance and Strategy Consulting</p>
    <p class="sectors">Aviation | Manufacturing | Energy</p>
  </section>
</main>
</body>
</html>
```